Business Cards and Logo needed for Rum Website

I need a smart, modern but fun business card (and Logo) to help promote my website BrightBarrelNotes.com

The website contains reviews of Rum (and eventually other spirits) as well as news and blog posts.

I would like a 2-sided design, with the logo and company name on one side and text on the other.

Text fields required are:
Name (Dan Fowler)
Website (www.brightbarrelnotes.com)
Email (dan@brightbarrelnotes.com)
Twitter (@BrightBarrelNotes)

For the logo i'm open to suggestions however it must incorporate a wooden Cask and a number of Stars. Ideas so far have been for a Cask surrounded in a number of Stars forming a circle around it with the text Bright Barrel Notes underneath. The logo should be modern but also a little bit cartoony and stylised. General drink/spirits themes will also be considered.

Colours: I like the idea of yellow text with black background but again i'm open to suggestions on what would work well. Contrasting colours for the 2-sides would be good.

Cards will be printed via Pelv.com so please consult their style guidelines if required: http://uk.pelv.com/help/faq/templates-and-guidelines.html

Requirements
Must have
• A spirits Cask
A number of Stars (preferrably yellow or gold)

```html
<!DOCTYPE html>
<html lang="en">
<head>
<meta charset="utf-8">
<title>Bright Barrel Notes – Business Card</title>
<link href="https://fonts.googleapis.com/css2?family=Ubuntu:wght@400;500;700&display=swap" rel="stylesheet">
<style>
  :root {
    --backdrop: #95a1a6;
    --card-yellow: #ffe510;
    --card-black: #000000;
    --ink-black: #111111;
    --ink-white: #ffffff;
    --ink-yellow: #f3dc17;
    --card-shadow: rgba(0, 0, 0, 0.55);
  }
  * { margin: 0; padding: 0; box-sizing: border-box; }
  html, body {
    width: 1200px;
    height: 900px;
    overflow: hidden;
    background: var(--backdrop);
    font-family: "Ubuntu", sans-serif;
  }
  .stage { position: relative; width: 1200px; height: 900px; }
  .card {
    position: absolute;
    left: 320px;
    width: 563px;
    height: 370px;
    border-radius: 38px;
    box-shadow: 6px 7px 6px var(--card-shadow);
  }
  .card--front { top: 60px; background: var(--card-yellow); }
  .card--back { top: 468px; background: var(--card-black); }

  .brand {
    position: absolute;
    display: flex;
    align-items: center;
  }
  .brand__mark { border-radius: 50%; flex: none; }
  .brand__name {
    font-weight: 700;
    text-transform: uppercase;
    line-height: 1.15;
  }
  .card--front .brand { left: 180px; top: 120px; gap: 26px; }
  .card--front .brand__mark { width: 92px; height: 92px; background: var(--ink-black); }
  .card--front .brand__name { font-size: 27px; color: var(--ink-black); }

  .card--back .brand { left: 218px; top: 52px; gap: 20px; }
  .card--back .brand__mark { width: 66px; height: 66px; background: var(--ink-yellow); }
  .card--back .brand__name { font-size: 19px; color: var(--ink-white); }

  .holder-name {
    position: absolute;
    top: 186px;
    width: 100%;
    text-align: center;
    font-size: 22px;
    font-weight: 500;
    color: var(--ink-white);
  }
  .contact {
    position: absolute;
    left: 40px;
    display: flex;
    align-items: center;
    gap: 11px;
    font-size: 19.5px;
    color: var(--ink-yellow);
  }
  .contact--twitter { top: 246px; }
  .contact--email { top: 273px; }
  .contact__icon { width: 14px; height: 12px; flex: none; }
  .contact__square { width: 11px; height: 11px; background: var(--ink-yellow); flex: none; margin: 0 1.5px; }
  .tagline {
    position: absolute;
    left: 345px;
    top: 273px;
    font-size: 19.5px;
    color: var(--ink-yellow);
  }
  .website {
    position: absolute;
    top: 310px;
    width: 100%;
    text-align: center;
    font-size: 19.5px;
    color: var(--ink-white);
  }
</style>
</head>
<body>
<main class="stage">
  <section class="card card--front" aria-label="Card front">
    <div class="brand">
      <span class="brand__mark"></span>
      <span class="brand__name">Bright<br>Barrel<br>Notes</span>
    </div>
  </section>

  <section class="card card--back" aria-label="Card back">
    <div class="brand">
      <span class="brand__mark"></span>
      <span class="brand__name">Bright<br>Barrel<br>Notes</span>
    </div>
    <p class="holder-name">Dan Fowler</p>
    <p class="contact contact--twitter"><span class="contact__square"></span>@BrightBarrelNotes</p>
    <p class="contact contact--email">
      <svg class="contact__icon" viewBox="0 0 14 12" aria-hidden="true">
        <rect x="0.5" y="1.5" width="13" height="9" fill="var(--ink-yellow)"/>
        <path d="M0.5 1.5 L7 7 L13.5 1.5" fill="none" stroke="#000" stroke-width="1.3"/>
      </svg>dan@brightbarrelnotes.com</p>
    <p class="tagline">rum &amp; other spirits</p>
    <p class="website">www.brightbarrelnotes.com</p>
  </section>
</main>
</body>
</html>
```